Solar Energy Technology Company - Solar Savings Analysis Flyer

I Have Included The Text Content I Want Put On An 8 1/2 " x 11" Flyer.

I Want To See It In One Page Format And In Tri-Fold Brochure Format.

It Needs To Grab And Captivate Prospective Customers, Awesome Graphics, Layout, Etc.

We Are A Cutting Edge Solar Energy Solutions & Technology Company.

We Need A World Class High Tech Look and Logo For Our Company Included On Our 8 1/2 x 11 Flyer & Trifold Brochure

Brightfold Venture Partners, LLC
"Forward Ideas Delivered"

Would Like A Black Gold And Electric Blue Color Scheme, However, We We Are Open To Seeing Your Creativity, Colors, Graphics Etc. For Consideration.

Target Market(s)

Homeowners Without Solar Panels On Their Roof

Industry/Entity Type

New Roof Top Solar Energy Producing Panel Technology Systems

Font styles to use
Serif

Requirements
Must have
• See My Attached Flyer/Trifold Brochure Display Content
Nice to have
• Gold Black And Electric Blue Color Scheme, Solar Theme Background Graphics

```html
<!DOCTYPE html>
<html lang="en">
<head>
<meta charset="utf-8">
<title>Bright Solar Gains – Solar Savings Flyer</title>
<link rel="stylesheet" href="https://fonts.googleapis.com/css2?family=Montserrat:wght@600;700;800&family=Roboto+Condensed:wght@400;700&family=Oswald:wght@500;600;700&family=Exo+2:wght@400;700&display=swap">
<style>
  :root {
    --page-bg: #7a7a7a;
    --paper: #ffffff;
    --blue: #4a65b8;
    --navy: #151a33;
    --orange: #ef8a1c;
    --orange-deep: #e8692c;
    --peach: #fcebe3;
    --ink: #111111;
    --ink-soft: #2a2a2a;
    --white: #ffffff;
  }
  * { box-sizing: border-box; margin: 0; padding: 0; }
  html, body { width: 1200px; height: 1200px; overflow: hidden; }
  body { background: var(--page-bg); position: relative; }

  .flyer {
    position: absolute; left: 190px; top: 20px;
    width: 820px; height: 1160px;
    background: linear-gradient(160deg, var(--paper) 55%, var(--peach) 100%);
    overflow: hidden;
  }

  .hero-photo {
    position: absolute; left: 0; top: 0; width: 820px; height: 600px;
    background:
      linear-gradient(180deg, rgba(255,255,255,0) 74%, var(--paper) 100%),
      radial-gradient(ellipse at 78% 88%, rgba(240,150,60,.55) 0%, rgba(240,150,60,0) 38%),
      linear-gradient(180deg, var(--blue) 0%, #3b4fa0 22%, #2b3570 45%, var(--navy) 68%, #0a0a10 82%);
  }

  .brand {
    position: absolute; left: 60px; top: 28px;
    font: 700 42px/1 "Roboto Condensed", sans-serif;
    color: var(--white); letter-spacing: .3px;
  }

  .attention-badge {
    position: absolute; right: 0; top: 0; width: 183px; height: 92px;
    background: var(--orange); border-bottom-left-radius: 22px;
    display: flex; align-items: center; justify-content: center; text-align: center;
    font: 700 19px/1.05 "Roboto Condensed", sans-serif; color: var(--white);
  }

  .headline-panel { position: absolute; left: 0; top: 86px; width: 450px; height: 226px; }
  .headline-panel svg { position: absolute; inset: 0; }
  .headline-text {
    position: absolute; left: 60px; top: 12px;
    font: 700 37px/36px "Montserrat", sans-serif; color: var(--white);
  }
  .headline-text .offer { color: var(--ink); font-size: 41px; line-height: 42px; display: block; margin-top: 4px; }

  .sub-headline {
    position: absolute; left: 62px; top: 326px;
    font: 700 25px/31px "Montserrat", sans-serif; color: var(--orange);
  }
  .savings-range {
    position: absolute; left: 60px; top: 414px;
    font: 800 46px/1 "Montserrat", sans-serif; color: var(--white); letter-spacing: -2px;
  }
  .tagline {
    position: absolute; left: 45px; top: 468px; width: 720px; text-align: center;
    font: 700 40px/1 "Oswald", sans-serif; color: var(--orange);
    -webkit-text-stroke: 1.5px var(--ink); paint-order: stroke fill;
  }
  .intro-copy {
    position: absolute; left: 55px; top: 526px; width: 710px;
    font: 400 14.5px/20px "Exo 2", sans-serif; color: var(--ink-soft); text-align: justify;
  }
  .intro-copy strong { color: var(--ink); font-weight: 700; font-size: 16px; }

  .savings-table {
    position: absolute; left: 55px; top: 594px; width: 711px;
    border: 2px solid var(--orange-deep); border-collapse: collapse;
    font-family: "Roboto Condensed", sans-serif;
  }
  .savings-table th {
    background: var(--orange-deep); color: var(--white); text-align: left;
    font: 700 17px/1 "Roboto Condensed", sans-serif; height: 36px; padding: 0 10px;
  }
  .savings-table td {
    height: 37.5px; padding: 0 10px; border-top: 2px solid var(--orange-deep);
    font: 700 18px/1 "Roboto Condensed", sans-serif; color: var(--ink);
    background: rgba(255,255,255,.55);
  }
  .savings-table td small { font: 400 13px/1 "Exo 2", sans-serif; margin-left: 4px; }

  .offer-copy {
    position: absolute; left: 54px; top: 846px; width: 712px;
    font: 400 14.5px/20px "Exo 2", sans-serif; color: var(--ink-soft); text-align: justify;
  }
  .offer-copy strong { color: var(--ink); font-weight: 700; }

  .web-bar {
    position: absolute; left: 52px; top: 937px; width: 708px; height: 45px;
    background: linear-gradient(180deg, #333 0%, #000 60%); border-radius: 5px;
    display: flex; align-items: center; justify-content: center;
    font: 700 27px/1 "Exo 2", sans-serif; color: var(--white); letter-spacing: 6px;
  }
  .cta-line {
    position: absolute; left: 54px; top: 994px;
    font: 600 20.5px/1 "Oswald", sans-serif; color: var(--ink); letter-spacing: -.3px;
  }
  .cta-line span { color: var(--orange-deep); }

  .contact-phone {
    position: absolute; left: 44px; top: 1052px;
    font: 800 23px/1 "Montserrat", sans-serif; color: var(--ink);
  }
  .contact-name {
    position: absolute; left: 44px; top: 1080px; width: 290px;
    font: 700 44px/1 "Roboto Condensed", sans-serif; color: var(--orange-deep);
    white-space: nowrap;
  }
  .contact-divider { position: absolute; left: 346px; top: 1056px; width: 2px; height: 70px; background: var(--orange-deep); }
  .company { position: absolute; left: 370px; top: 1052px; font-family: "Roboto Condensed", sans-serif; }
  .company-name { font: 700 21px/1 "Roboto Condensed", sans-serif; color: var(--orange-deep); margin-bottom: 6px; }
  .company-office { font: 400 17px/23px "Roboto Condensed", sans-serif; color: var(--ink); }
  .company-office b { font-weight: 700; }

  .footer-band { position: absolute; left: 0; bottom: 0; width: 820px; height: 12px; display: flex; gap: 5px; }
  .footer-band i { display: block; height: 100%; background: var(--orange); }
  .footer-band i.deep { background: var(--orange-deep); }
</style>
</head>
<body>
<main class="flyer">
  <div class="hero-photo" role="img" aria-label="Dusk photo of a house with dark blue solar panels covering its roof and warm lit windows"></div>

  <div class="brand">BRIGHT SOLAR GAINS</div>
  <div class="attention-badge">ATTENTION<br>HOMEOWNER!</div>

  <div class="headline-panel">
    <svg width="450" height="226" viewBox="0 0 450 226" aria-hidden="true">
      <polygon points="0,0 440,0 410,226 0,226" fill="#ef8a1c"/>
    </svg>
    <h1 class="headline-text">ARE YOU FED UP<br>WITH YOUR HIGH<br>ELECTRIC BILLS?<span class="offer">WE WILL PAY<br>YOU $2,000…</span></h1>
  </div>

  <p class="sub-headline">WHEN YOU ALLOW US TO<br>PERMANENTLY LOWER YOUR<br>ELECTRIC BILL BY AT LEAST</p>
  <p class="savings-range">25% TO 50%!</p>
  <p class="tagline">“FORWARD IDEAS DELIVERED”</p>

  <p class="intro-copy">On Average, We Savehomeowners <strong>*33%OFF</strong> Their Electricity Cost Every Month With Our New Cutting Edge Advanced Solar Technology,Without Taking 1 Penny From Your Current Monthly Budget. Government Subsidized!</p>

  <table class="savings-table">
    <thead><tr><th>*IF YOUR Last12 Months “Average Monthly Electric Payment” Is...</th></tr></thead>
    <tbody>
      <tr><td>*$100: Your NEW Monthly Fixed Payment Will Be $67 <small>($396 Annual Savings)</small></td></tr>
      <tr><td>*$200: Your NEW Monthly Fixed Payment Will Be $134 <small>($792 Annual Savings)</small></td></tr>
      <tr><td>*$300: Your NEW Monthly Fixed Payment Will Be $201 <small>($1,188 Annual Savings)</small></td></tr>
      <tr><td>*$400: Your NEW Monthly Fixed Payment Will Be $268 <small>($1,584 Annual Savings)</small></td></tr>
      <tr><td>*$500: Your NEW Monthly Fixed Payment Will Be $335 <small>($1,980 Annual Savings)</small></td></tr>
    </tbody>
  </table>

  <p class="offer-copy">IF YOU OWN YOUR HOME, WE WILL SEND YOU OUR <strong>“NOBEL PRIZE WINNING TECHNOLOGY”</strong> THAT WILL <strong>ELIMINATE $200 OF YOUR GAS OR DIESEL FUEL EXPENSE</strong> When You Allow Us To <strong>Do A NO COST, NO OBLIGATION ENERGY SAVINGS ANALYSIS</strong> And Share YOUR MONEY <strong>SAVING RESULTS</strong> With You Via A 30 Minute Video Meeting.</p>

  <div class="web-bar">WWW.BRIGHTSOLARGAINS.ENERGY</div>
  <p class="cta-line">TO REQUEST YOUR COMPLIMENTARY ENERGY SAVINGS ANALYSIS &amp; TO <span>ACCEPT OUR $200 GIFT.</span></p>

  <p class="contact-phone">888-555-0142 EXT. 210</p>
  <p class="contact-name">DANA MORROW</p>
  <div class="contact-divider"></div>
  <div class="company">
    <p class="company-name">BRIGHTFOLD VENTURE PARTNERS, LLC</p>
    <p class="company-office"><b>CORP OFFICE:</b> 4120 Canyon Ridge Blvd. Las Vegas, NV 89101</p>
    <p class="company-office"><b>REGIONAL OFFICE:</b> 1560 Orchard Lane Clovis, CA 93612</p>
  </div>

  <div class="footer-band" aria-hidden="true">
    <i style="width:36px"></i><i style="width:276px"></i><i class="deep" style="width:498px"></i>
  </div>
</main>
</body>
</html>
```